Clean professional design needed for landscape property business

We need a logo for a new lawncare, landscaping , property maintenance business called Meadow Trim.
Our services include lawn mowing, garden maintenance, clean ups and some property maintenance.
We want a double sided business card that is clean and very professional using the colour scheme from our logo which is provided.
the business card should have impact as we will use these to drop into people's letterboxes as a marketing drop.
Initially we want to see what you come up with so there is a very wide scope here to work with.
Updates

Project Deadline Extended
Reason: we feel our original deadline was too short. we have extended to give more time for quality submissions.

Target Market(s)

High end property owners who don't wish to do there own gardneing or property maintenance

Industry/Entity Type

Business

Contact Information for Business Card

Name
Postion/ Title
Phone number
mobile
web address
physical address

services offered

Font styles to use
Sans Serif

Requirements
Must have
• curved edges preferrred
Nice to have
• We like the idea of the logo being embossed or etched into the card so it looks like it is below the surface of the card
Should not have
• No stock images or characters.

```html
<!DOCTYPE html>
<html lang="en">
<head>
<meta charset="utf-8">
<title>Meadow Trim – Business Card</title>
<link rel="stylesheet" href="https://fonts.googleapis.com/css2?family=Roboto:wght@700;900&family=Open+Sans:wght@400;600&display=swap">
<style>
  :root {
    --stage: #5b5b5d;
    --card-dark: #58585a;
    --card-light: #ffffff;
    --leaf-green: #7bc014;
    --ink-white: #ffffff;
    --ink-soft: #e6e6e6;
    --divider: #d8d8d8;
  }
  * { box-sizing: border-box; margin: 0; padding: 0; }
  html, body { width: 1200px; height: 900px; overflow: hidden; }
  body {
    background: var(--stage);
    position: relative;
    font-family: "Open Sans", sans-serif;
  }
  .card {
    position: absolute;
    left: 300px;
    width: 600px;
    height: 343px;
    border-radius: 28px;
    overflow: hidden;
    box-shadow: 0 10px 28px rgba(0,0,0,0.35);
  }
  .card--front { top: 70px; background: var(--card-dark); }
  .card--back { top: 487px; background: var(--card-light); }

  .brand {
    position: absolute;
    display: flex;
    align-items: center;
    gap: 14px;
    font-family: "Roboto", sans-serif;
    font-weight: 900;
    letter-spacing: -2px;
    white-space: nowrap;
  }
  .brand__mark {
    width: 18px;
    height: 18px;
    flex: none;
  }
  .card--front .brand {
    left: 0; right: 0; top: 0; bottom: 0;
    justify-content: center;
    font-size: 64px;
    color: var(--ink-white);
  }
  .card--front .brand__mark { background: var(--leaf-green); }

  .card--back .brand {
    left: 150px;
    top: 40px;
    font-size: 54px;
    color: var(--card-dark);
  }
  .card--back .brand__mark { background: var(--leaf-green); }

  .swoosh { position: absolute; inset: 0; width: 100%; height: 100%; }

  .person {
    position: absolute;
    left: 118px;
    top: 232px;
    text-align: right;
    width: 170px;
  }
  .person__name {
    font-family: "Roboto", sans-serif;
    font-weight: 700;
    font-size: 24px;
    color: var(--leaf-green);
    letter-spacing: -0.5px;
  }
  .person__title {
    font-family: "Roboto", sans-serif;
    font-weight: 700;
    font-size: 13px;
    color: var(--ink-white);
    margin-top: 2px;
  }
  .divider {
    position: absolute;
    left: 305px;
    top: 190px;
    width: 1.5px;
    height: 118px;
    background: var(--divider);
  }
  .contact {
    position: absolute;
    left: 322px;
    top: 186px;
    color: var(--ink-soft);
    font-size: 13px;
    line-height: 1.45;
  }
  .contact__address { margin-bottom: 8px; }
  .contact__row { display: flex; align-items: center; gap: 8px; }
  .contact__icon { width: 12px; height: 12px; flex: none; }
</style>
</head>
<body>

<section class="card card--front">
  <div class="brand">
    <span class="brand__name">Meadow Trim</span>
    <span class="brand__mark"></span>
  </div>
</section>

<section class="card card--back">
  <svg class="swoosh" viewBox="0 0 600 343" preserveAspectRatio="none" aria-hidden="true">
    <path d="M0 268 C140 150 360 120 600 112 L600 343 L0 343 Z" fill="#7bc014"/>
    <path d="M0 290 C150 175 360 140 600 128 L600 343 L0 343 Z" fill="#58585a"/>
  </svg>

  <div class="brand">
    <span class="brand__name">Meadow Trim</span>
    <span class="brand__mark"></span>
  </div>

  <div class="person">
    <div class="person__name">DANIEL REYES</div>
    <div class="person__title">CEO/FOUNDER</div>
  </div>

  <div class="divider"></div>

  <div class="contact">
    <div class="contact__address">1180 Willow Bend Rd<br>Fairview, TX.USA</div>
    <div class="contact__row">
      <svg class="contact__icon" viewBox="0 0 12 12" aria-hidden="true"><rect x="1" y="4" width="10" height="7" rx="1.5" fill="#7bc014"/><path d="M1 4 Q6 0 11 4" stroke="#7bc014" stroke-width="1.6" fill="none"/></svg>
      <span>+1 555-014-2273</span>
    </div>
    <div class="contact__row">
      <svg class="contact__icon" viewBox="0 0 12 12" aria-hidden="true"><path d="M2 1 L4.5 1 L5.5 3.5 L4 4.8 Q5 7.2 7.2 8 L8.5 6.5 L11 7.5 L11 10 Q11 11 10 11 Q1 10 1 2 Q1 1 2 1 Z" fill="#7bc014"/></svg>
      <span>+1 555-014-2274</span>
    </div>
    <div class="contact__row">
      <svg class="contact__icon" viewBox="0 0 12 12" aria-hidden="true"><circle cx="6" cy="6" r="5" fill="none" stroke="#7bc014" stroke-width="1.4"/><path d="M1 6 H11 M6 1 Q3 6 6 11 M6 1 Q9 6 6 11" stroke="#7bc014" stroke-width="1" fill="none"/></svg>
      <span>www.meadowtrim.com</span>
    </div>
  </div>
</section>

</body>
</html>
```